Casa Vero Inspections Business Card

I need a business card for my new company. The company is going to provide home inspections. The name of the company is Casa Vero Inspections. I am not sure if I want a single sided card or a double. I have a logo already that I want to incorporate into the card design. I was wondering if I should incorporate a catch phrase on my card or not. If I did the phrase would be "The Trusted Standard for Home Inspections" but i am unsure how or if to use it on a card. The following information needs to be on the card.
Home Inspection
My Name: Marcus T. Wolford Phone Number: 555-301-7762 Email: mwolford@casaveroinspections.com Website: www.casaveroinspections.com NY HI License # 27300519462

```html
<!DOCTYPE html>
<html lang="en">
<head>
<meta charset="utf-8">
<title>Casa Vero Inspections – Business Card</title>
<link rel="stylesheet" href="https://fonts.googleapis.com/css2?family=Open+Sans:ital,wght@0,400;0,600;0,700;0,800;1,400&display=swap">
<style>
  :root {
    --page-bg: #232323;
    --card-dark: #1e1e21;
    --card-blue: #116aa8;
    --brand-blue: #1b73b8;
    --brand-deep: #0d5a92;
    --brand-light: #4aa3dc;
    --text-light: #f2f2f2;
    --divider: #1f6aa6;
  }
  * { box-sizing: border-box; margin: 0; padding: 0; }
  html, body {
    width: 1200px; height: 780px; overflow: hidden;
    background: var(--page-bg);
    font-family: "Open Sans", Arial, sans-serif;
  }
  .canvas {
    position: relative; width: 1200px; height: 780px;
    display: flex; align-items: center; justify-content: center; gap: 50px;
  }
  .card {
    position: relative; width: 525px; height: 300px;
    border-radius: 22px; overflow: hidden;
    box-shadow: 0 14px 30px rgba(0,0,0,.45);
  }
  /* Front */
  .card-front { background: var(--card-dark); color: var(--text-light); }
  .front-brand {
    position: absolute; left: 34px; top: 70px; width: 200px;
    display: flex; align-items: center; gap: 10px;
  }
  .brand-mark { width: 14px; height: 14px; background: var(--brand-blue); flex: none; }
  .brand-name {
    font-weight: 800; font-size: 22px; line-height: 1.15;
    color: var(--brand-blue); text-transform: uppercase; letter-spacing: .5px;
  }
  .license {
    position: absolute; left: 36px; top: 200px;
    font-size: 12.5px; color: var(--text-light); white-space: nowrap;
  }
  .license-label { color: var(--brand-light); }
  .divider { position: absolute; left: 0; top: 0; width: 525px; height: 300px; }
  .contact-block { position: absolute; left: 290px; top: 92px; }
  .person-name { font-weight: 700; font-size: 24px; color: var(--brand-blue); line-height: 1.1; white-space: nowrap; }
  .person-role { font-size: 13px; color: var(--text-light); margin-top: 4px; margin-bottom: 14px; }
  .contact-list { list-style: none; }
  .contact-item {
    display: flex; align-items: center; gap: 8px;
    font-size: 11px; line-height: 1; margin-bottom: 8px; white-space: nowrap;
  }
  .contact-icon { width: 12px; height: 12px; flex: none; }
  /* Back */
  .card-back {
    background: var(--card-blue);
    display: flex; flex-direction: column; align-items: center; justify-content: center;
  }
  .back-brand { display: flex; align-items: center; gap: 12px; }
  .back-brand .brand-mark { width: 18px; height: 18px; background: var(--brand-deep); }
  .back-brand .brand-name { font-size: 30px; color: var(--brand-deep); white-space: nowrap; }
  .tagline {
    margin-top: 18px; font-style: italic; font-size: 13.5px; color: var(--text-light);
  }
</style>
</head>
<body>
<main class="canvas">
  <section class="card card-front" aria-label="Business card front">
    <div class="front-brand">
      <span class="brand-mark"></span>
      <span class="brand-name">Casa Vero Inspections</span>
    </div>
    <p class="license"><span class="license-label">NY HI License #</span> 27300519462</p>
    <svg class="divider" viewBox="0 0 525 300" aria-hidden="true">
      <line x1="272" y1="45" x2="212" y2="265" stroke="var(--divider)" stroke-width="1"/>
    </svg>
    <div class="contact-block">
      <h1 class="person-name">Marcus T. Wolford</h1>
      <p class="person-role">Co-Founder</p>
      <ul class="contact-list">
        <li class="contact-item">
          <svg class="contact-icon" viewBox="0 0 24 24" aria-hidden="true"><path fill="var(--brand-light)" d="M6.6 10.8a15 15 0 0 0 6.6 6.6l2.2-2.2a1 1 0 0 1 1-.25 11.4 11.4 0 0 0 3.6.57 1 1 0 0 1 1 1V20a1 1 0 0 1-1 1A17 17 0 0 1 3 4a1 1 0 0 1 1-1h3.5a1 1 0 0 1 1 1c0 1.25.2 2.45.57 3.57a1 1 0 0 1-.25 1z"/></svg>
          555-301-7762
        </li>
        <li class="contact-item">
          <svg class="contact-icon" viewBox="0 0 24 24" aria-hidden="true"><circle cx="12" cy="12" r="10" fill="none" stroke="var(--brand-light)" stroke-width="2"/><path d="M2 12h20M12 2c3 3 3 17 0 20M12 2c-3 3-3 17 0 20" fill="none" stroke="var(--brand-light)" stroke-width="1.6"/></svg>
          www.casaveroinspections.com
        </li>
        <li class="contact-item">
          <svg class="contact-icon" viewBox="0 0 24 24" aria-hidden="true"><rect x="2" y="5" width="20" height="14" rx="1.5" fill="none" stroke="var(--brand-light)" stroke-width="2"/><path d="M2 6l10 7 10-7" fill="none" stroke="var(--brand-light)" stroke-width="2"/></svg>
          mwolford@casaveroinspections.com
        </li>
      </ul>
    </div>
  </section>

  <section class="card card-back" aria-label="Business card back">
    <div class="back-brand">
      <span class="brand-mark"></span>
      <span class="brand-name">Casa Vero Inspections</span>
    </div>
    <p class="tagline">The Trusted Standard for Home Inspections</p>
  </section>
</main>
</body>
</html>
```